INNOVATION WEBSITE NEEDED: Agency from NZ needs YOU

Please see the enclosed documents for a detailed brief. It needs to be clean / simple / elegant / premium looking - that will appeal to companies that range from start-up to multi-national!
Note:
Perhaps instead of an actual shop, people can press an 'enquire now' button?

Target Market(s)

Start ups to multi-nationals

Industry/Entity Type

Marketing

Number of Pages Required

5+ page

Requirements
Must have
• Wordpress
• SEO
• Format friendly (mobile / tablet / etc)
• I have the URL: www.qu-tessaroly.com - I would like a working website. Please let me know what else you require to 'go live' with. Thanks!
Nice to have
• Please use / improve on my current ideas
• Perhaps use my logo icon (in different colours) for each 'product'?

```html
<!DOCTYPE html>
<html lang="en">
<head>
<meta charset="utf-8">
<title>Qu-Tessaroly – Creating the Future</title>
<link rel="stylesheet" href="https://fonts.googleapis.com/css2?family=Raleway:wght@400;500;600;700&family=Gilda+Display&display=swap">
<style>
:root{
  --navy:#2b2566;
  --navy-deep:#221d55;
  --blue:#29a8e0;
  --ink:#222;
  --muted:#555;
  --dark:#1d2024;
  --footer:#25272a;
  --white:#fff;
  --serif:"Gilda Display", Georgia, serif;
  --sans:"Raleway", Arial, sans-serif;
}
*{box-sizing:border-box;margin:0;padding:0}
html,body{width:1200px;height:2293px;overflow:hidden}
body{font-family:var(--sans);color:var(--ink);background:var(--white);position:relative}
.wrap{width:702px;margin-left:249px;position:relative}
.photo{display:block}

/* top bar */
.topbar{height:17px;background:var(--navy);color:#fff;font-size:8px;display:flex;align-items:center}
.topbar .wrap{display:flex;justify-content:space-between}
.topbar b{font-weight:700}
.topbar nav{display:flex;gap:24px;text-transform:uppercase;font-weight:600}
/* header */
.header{height:64px;background:linear-gradient(#f2f2f2,#e2e2e2)}
.header .wrap{display:flex;justify-content:space-between;align-items:center;height:64px}
.brand{display:flex;align-items:center;gap:8px}
.brand-mark{width:26px;height:26px;background:var(--navy);border-radius:50%}
.brand-name{font-family:var(--sans);font-weight:700;color:var(--navy);font-size:13px;letter-spacing:.5px}
.contacts{display:flex;height:44px}
.contact-chip{display:flex;align-items:center;gap:9px;padding:0 14px;font-size:9px;border-left:1px solid #ccc}
.contact-chip:first-child{border:none}
.ico{width:30px;height:30px;border-radius:50%;background:var(--navy);display:flex;align-items:center;justify-content:center}
.ico svg{width:15px;height:15px;fill:#fff}
/* hero */
.hero{height:327px;background:linear-gradient(90deg,#d9d9d9,#f3f3f3 40%,#c9cbcd 75%,#b3b5b7);position:relative}
.hero-quote{position:absolute;left:249px;top:105px;width:410px;text-align:center;font-size:21px;line-height:27px;color:var(--navy);font-weight:500}
.hero-quote em{font-style:normal;color:var(--blue)}
.btn-fill{display:inline-block;background:var(--blue);color:#fff;font-size:11px;font-weight:600;line-height:13px;padding:7px 18px;text-transform:uppercase;text-align:center;white-space:nowrap}
.hero .btn-fill{margin-top:18px;width:94px;padding:7px 0}
.dots{position:absolute;left:865px;top:312px;display:flex;gap:8px}
.dots i{width:24px;height:3px;background:var(--navy)}
.dots i:nth-child(2){background:var(--blue)}
/* nav */
.mainnav{height:40px;background:#fff;position:relative;border-bottom:1px solid #ddd}
.mainnav ul{list-style:none;display:flex;margin-left:249px;height:40px}
.mainnav li{padding:0 10px;display:flex;align-items:center;font-size:11px;font-weight:600;text-transform:uppercase}
.mainnav li.active{background:var(--blue);color:#fff;padding:0 14px}
.social-band{position:absolute;right:0;top:0;width:420px;height:40px;background:var(--blue);clip-path:polygon(40px 0,100% 0,100% 100%,0 100%);display:flex;align-items:center;gap:18px;padding-left:70px}
.social-band i{width:16px;height:16px;border-radius:50%;background:#fff}
/* services */
.services{height:502px;background:linear-gradient(180deg,#24282c,#16191c);position:relative}
.section-title{font-family:var(--serif);font-size:30px;text-align:center;color:#fff;letter-spacing:1px;font-weight:400}
.section-title span{color:var(--blue)}
.services .section-title{padding-top:15px}
.cards{display:flex;gap:27px;margin:23px 0 0 249px}
.card{width:216px;background:#fff}
.card .photo{height:187px;background:linear-gradient(135deg,#2a3340,#8a96a4)}
.card h3{font-family:var(--serif);font-weight:400;font-size:22px;color:var(--navy);text-align:center;margin-top:10px}
.card p{font-size:9px;line-height:14px;text-align:center;padding:6px 18px 10px;color:#333;height:84px}
.price-bar{height:52px;background:var(--navy-deep);display:flex;align-items:center;justify-content:space-between;padding:0 18px;color:#fff}
.price{font-size:17px;color:var(--blue)}
.price b{font-weight:500;color:#fff}
.btn-line{border:1px solid #fff;color:#fff;font-size:10px;padding:6px 14px;text-transform:uppercase;white-space:nowrap}
.services .btn-fill{position:absolute;left:543px;top:452px;width:116px;padding:7px 0}
/* how it works */
.gap{height:19px;background:#fff}
.how{height:326px;display:flex;background:linear-gradient(90deg,#fff,#eee)}
.how-text{width:538px;flex:none;padding:10px 0 0 249px}
.how-text h2{font-family:var(--serif);font-weight:400;font-size:29px;color:var(--navy);margin-bottom:8px}
.how-text p{font-size:10.5px;line-height:15.5px;color:#222;margin-bottom:12px;width:252px}
.how-photo{flex:1;background:linear-gradient(135deg,#b9c6d2,#e9e4dc 50%,#8a8f96);position:relative}
.how-photo .arrow{position:absolute;left:-28px;bottom:0;width:28px;height:28px;background:var(--navy);display:flex;align-items:center;justify-content:center}
.how-photo .arrow svg{width:12px;height:12px;stroke:#fff;fill:none;stroke-width:2.5}
/* info boxes */
.info{height:324px;padding-top:20px}
.boxes{display:flex;gap:27px;margin-left:249px}
.box{width:216px;height:283px;border:1px solid #ccc;position:relative}
.box h4{background:var(--navy);color:#fff;font-family:var(--serif);font-weight:400;font-size:16px;padding:5px 6px;height:31px}
.box .photo{height:87px;margin:4px;background:linear-gradient(135deg,#c9ccd1,#6b7078)}
.box p{font-size:9.5px;line-height:13px;padding:3px 6px;color:#222}
.box strong{font-weight:600}
.box ul{list-style:none;padding:0 6px}
.box li{font-size:9.5px;line-height:13px;margin-bottom:5px;padding-left:12px;position:relative}
.box li::before{content:"";position:absolute;left:1px;top:3px;width:6px;height:3px;border-left:1.5px solid var(--blue);border-bottom:1.5px solid var(--blue);transform:rotate(-45deg)}
.box .btn-line{position:absolute;right:12px;bottom:8px;color:var(--navy);border-color:var(--navy);font-size:11px;padding:6px 16px}
/* chat */
.chat{height:402px;background:linear-gradient(90deg,#2a2c2f,#1a1c1f 50%,#2d2f32);position:relative;color:#fff}
.chat h2{font-family:var(--serif);font-weight:400;font-size:30px;color:var(--blue);text-align:center;padding-top:28px}
.chat .lead{width:600px;margin:10px auto 0;text-align:center;font-size:10px;line-height:15px;color:#777}
.chat-list{position:absolute;left:249px;top:143px;list-style:none}
.chat-list li{display:flex;align-items:center;gap:18px;height:54px;font-size:11px;color:#bbb}
.chat-list .ico{width:38px;height:38px;background:#fff;flex:none}
.chat-list .ico svg{fill:var(--dark);width:18px;height:18px}
.chat-form{position:absolute;left:488px;top:148px;width:463px}
.chat-form h3{font-family:var(--serif);font-weight:400;font-size:26px;text-align:center;margin-bottom:30px}
.row{display:flex;gap:18px}
.field{flex:1;border-bottom:1px solid #aaa;font-size:9px;color:#999;padding:0 0 6px 4px;margin-bottom:40px}
.chat-form .btn-line{display:block;width:102px;margin:-16px auto 0 179px;text-transform:none;font-size:9px;text-align:center;border-color:#bbb;color:var(--blue)}
/* newsletter */
.newsletter{height:48px;background:#0c0c0c;display:flex;align-items:center;justify-content:center;gap:14px}
.newsletter h3{font-family:var(--serif);font-weight:400;color:#fff;font-size:19px}
.newsletter h3 span{color:var(--blue)}
.newsletter .email{width:193px;height:22px;background:#fff;font-size:8px;color:#888;padding:6px}
.newsletter .btn-line{font-size:10px;padding:4px 12px;margin-left:2px;border-color:#bbb;color:#fff}
/* footer */
.footer{height:191px;background:var(--footer);color:#fff;position:relative}
.col{position:absolute;top:24px}
.col h4{font-family:var(--serif);font-weight:400;font-size:18px;margin-bottom:14px}
.col h4 span{color:var(--blue)}
.sitemap{left:249px}
.sitemap ul{list-style:none}
.sitemap li{font-size:10px;line-height:17.5px;text-transform:uppercase}
.sitemap li.active{color:var(--blue)}
.posts{left:448px}
.feed{left:765px}
.item{display:flex;gap:12px;margin-bottom:16px;font-size:9px;line-height:12px;width:250px}
.item .thumb{width:52px;height:44px;flex:none;background:linear-gradient(135deg,#a78c70,#4a4040)}
.item .dot{width:16px;height:16px;border-radius:50%;background:var(--blue);flex:none;margin-top:2px}
.item time{display:block;color:var(--blue);font-size:8px;margin-top:2px}
.copyright{height:33px;background:var(--navy);color:#fff;font-size:9px;font-weight:600;display:flex;align-items:center}
</style>
</head>
<body>

<header>
  <div class="topbar">
    <div class="wrap">
      <span><b>Qu-Tessaroly</b> Creating the Future</span>
      <nav><span>My Account</span><span>Register</span><span>Terms and Conditions</span><span>FAQ</span><span>Support</span></nav>
    </div>
  </div>
  <div class="header">
    <div class="wrap">
      <div class="brand"><span class="brand-mark"></span><span class="brand-name">QU-TESSAROLY</span></div>
      <div class="contacts">
        <div class="contact-chip"><span class="ico"><svg viewBox="0 0 24 24"><path d="M6.6 10.8a15 15 0 0 0 6.6 6.6l2.2-2.2c.3-.3.7-.4 1-.2 1.1.4 2.3.6 3.6.6.6 0 1 .4 1 1V20c0 .6-.4 1-1 1A17 17 0 0 1 3 4c0-.6.4-1 1-1h3.5c.6 0 1 .4 1 1 0 1.3.2 2.5.6 3.6.1.3 0 .7-.2 1z"/></svg></span>+64 21 555 0142</div>
        <div class="contact-chip"><span class="ico"><svg viewBox="0 0 24 24"><circle cx="12" cy="12" r="6"/></svg></span>Qu-Tessaroly</div>
        <div class="contact-chip"><span class="ico"><svg viewBox="0 0 24 24"><path d="M3 6h18v12H3z M3 6l9 7 9-7" stroke="#2b2566" stroke-width="1.5"/></svg></span>Action@Qu-Tessaroly.com</div>
      </div>
    </div>
  </div>
  <section class="hero photo" role="img" aria-label="Photo of a young professional working at a laptop in a bright office">
    <div class="hero-quote">Finding it <em>hard to get</em> all the different functions aligned and therefore getting no where on innovation?”<br><span class="btn-fill">Buy Now</span></div>
    <div class="dots"><i></i><i></i><i></i></div>
  </section>
  <nav class="mainnav">
    <ul><li class="active">Home</li><li>Shop</li><li>Our Purpose</li><li>What We Do</li><li>The Team</li><li>Contact</li></ul>
    <div class="social-band"><i></i><i></i><i></i></div>
  </nav>
</header>

<main>
  <section class="services">
    <h2 class="section-title"><span>OUR</span> SERVICES</h2>
    <div class="cards">
      <article class="card">
        <div class="photo" role="img" aria-label="Hand drawing a glowing staircase towards a figure"></div>
        <h3>The Barista</h3>
        <p>Lorem Ipsum is simply dummy text of the printing and typesetting industry. Lorem Ipsum has been the industry's standard dummy text ever since the 1500s, when an</p>
        <div class="price-bar"><span class="price">$<b>FREE</b></span><span class="btn-line">Buy Now</span></div>
      </article>
      <article class="card">
        <div class="photo" role="img" aria-label="Business team joining hands in a huddle"></div>
        <h3>The Grand Knight</h3>
        <p>Lorem Ipsum is simply dummy text of the printing and typesetting industry. Lorem Ipsum has been the industry's standard dummy text ever since the 1500s, when an</p>
        <div class="price-bar"><span class="price">$<b>499</b></span><span class="btn-line">Buy Now</span></div>
      </article>
      <article class="card">
        <div class="photo" role="img" aria-label="Businessman touching a virtual screen of growth charts"></div>
        <h3>The Ninja</h3>
        <p>Lorem Ipsum is simply dummy text of the printing and typesetting industry. Lorem Ipsum has been the industry's standard dummy text ever since the 1500s, when an</p>
        <div class="price-bar"><span class="price">$<b>749</b></span><span class="btn-line">Buy Now</span></div>
      </article>
    </div>
    <span class="btn-fill">More Options</span>
  </section>

  <div class="gap"></div>

  <section class="how">
    <div class="how-text">
      <h2>How it Works</h2>
      <p>Instead of asking for a quote like with most agencies, we have a price list. You can order our services online!</p>
      <p>There's no back and forwards with long winded quotes that have taken your briefing, reworded it and sent it back to you with a huge price tag attached!<br>Simply have a look at our innovation shop window and if you like what you see and know exactly what you want, you push the 'Buy' button. And then we will start working.<br>If you want totalk beforehand, simply give the team at Qu-Tessaroly a call and we can have a quick chat first.</p>
    </div>
    <div class="how-photo photo" role="img" aria-label="Overhead view of a team meeting around a table with charts">
      <span class="arrow"><svg viewBox="0 0 12 12"><path d="M4 1l5 5-5 5"/></svg></span>
    </div>
  </section>

  <section class="info">
    <div class="boxes">
      <article class="box">
        <h4>Re boot or Kick start…?</h4>
        <div class="photo" role="img" aria-label="Team of colleagues in a bright office"></div>
        <p>Do you need to reboot or kick-start your company's innovation capabilities in terms of process, people or projects?</p>
        <p><strong>Do you need:</strong></p>
        <ul><li>A new way of doing something?</li><li>A brilliant breakthrough idea?</li><li>A 3-5 year roadmap of strategic innovation?</li></ul>
        <span class="btn-line">Read More</span>
      </article>
      <article class="box">
        <h4>Our Purpose</h4>
        <div class="photo" role="img" aria-label="Businessman beside a chalkboard with a motivational goal message"></div>
        <p><strong>Our purpose is to re-define how companies like yours get great innovation. Quickly.</strong></p>
        <p>The team at Qu-Tessaroly have worked both client side and as consultants. We know what works and how things tick internally. It's not just about pretty pictures. Ideas need to stack up: strategically, culturally and commercially.</p>
        <span class="btn-line">Read More</span>
      </article>
      <article class="box">
        <h4>What we do</h4>
        <div class="photo" role="img" aria-label="Colleagues gathered around a laptop"></div>
        <p>We innovate. For you.</p>
        <p><strong>The most common things we hear are:</strong></p>
        <ul><li>I need a breakthrough innovation, but am staring at a blank piece of paper</li><li>I have to come up with a great idea, but have a limited budget and little time</li></ul>
        <span class="btn-line">Read More</span>
      </article>
    </div>
  </section>

  <section class="chat" role="img" aria-label="Dimmed photo of a support team wearing headsets">
    <h2>Let’s have a chat</h2>
    <p class="lead">The team at Qu-Tessaroly is flexible in terms of time and location – using today's technology, we can be with you virtually anytime, anywhere. If you are in Europe, we can work while you sleep! Waiheke Island is one of the most beautiful, creative hot spots in New Zealand. It is an inspirational and innovation conducive locale and our offices can also be used for workshops.</p>
    <ul class="chat-list">
      <li><span class="ico"><svg viewBox="0 0 24 24"><path d="M6.6 10.8a15 15 0 0 0 6.6 6.6l2.2-2.2c.3-.3.7-.4 1-.2 1.1.4 2.3.6 3.6.6.6 0 1 .4 1 1V20c0 .6-.4 1-1 1A17 17 0 0 1 3 4c0-.6.4-1 1-1h3.5c.6 0 1 .4 1 1 0 1.3.2 2.5.6 3.6.1.3 0 .7-.2 1z"/></svg></span>+64 21 555 0142</li>
      <li><span class="ico"><svg viewBox="0 0 24 24"><circle cx="12" cy="12" r="7"/></svg></span>Qu-Tessaroly</li>
      <li><span class="ico"><svg viewBox="0 0 24 24"><path d="M3 6h18v12H3z M3 6l9 7 9-7" stroke="#fff" stroke-width="1.5"/></svg></span>Action@Qu-Tessaroly.com</li>
      <li><span class="ico"><svg viewBox="0 0 24 24"><path d="M12 2a7 7 0 0 0-7 7c0 5 7 13 7 13s7-8 7-13a7 7 0 0 0-7-7zm0 9.5a2.5 2.5 0 1 1 0-5 2.5 2.5 0 0 1 0 5z"/></svg></span>14 Harbour Lane, Oneroa Bay,<br>Waiheke Island, Auckland,<br>New Zealand</li>
    </ul>
    <form class="chat-form">
      <h3>Contact Now!</h3>
      <div class="row"><div class="field">Yor name here</div><div class="field">Yor mail here</div></div>
      <div class="field">Yor message here</div>
      <span class="btn-line">Send Message</span>
    </form>
  </section>
</main>

<footer>
  <div class="newsletter">
    <h3>Newsletter <span>Signup</span></h3>
    <div class="email">Email</div>
    <span class="btn-line">Signup</span>
  </div>
  <div class="footer">
    <div class="col sitemap">
      <h4>Site <span>Map</span></h4>
      <ul><li class="active">Home</li><li>Shop</li><li>Our Purpose</li><li>What We Do</li><li>The Team</li><li>Contact</li></ul>
    </div>
    <div class="col posts">
      <h4>Recent <span>Posts</span></h4>
      <div class="item"><div class="thumb photo" role="img" aria-label="Blog post thumbnail"></div><div>Lorem Ipsum is simply dummy text of the printing and typesetting industry.<time>March 2, 2014</time></div></div>
      <div class="item"><div class="thumb photo" role="img" aria-label="Blog post thumbnail"></div><div>Lorem Ipsum is simply dummy text of the printing and typesetting industry.<time>March 2, 2014</time></div></div>
    </div>
    <div class="col feed">
      <h4>Chirpline <span>Feed</span></h4>
      <div class="item"><span class="dot"></span><div>Lorem Ipsum is simply dummy text of the printing and typesetting industry.<time>5 Hour Ago</time></div></div>
      <div class="item"><span class="dot"></span><div>Lorem Ipsum is simply dummy text of the printing and typesetting industry.<time>5 Hour Ago</time></div></div>
    </div>
  </div>
  <div class="copyright"><div class="wrap">© Copyright 2016 QU-TESSAROLY</div></div>
</footer>

</body>
</html>
```